Wholesale e-commerce website re-design

We are a wholesaler of African-made and African-themed products, and we're looking to update the look and feel of our website www.lomatrade.com to improve user experience. We'd like to have a cleaner homepage that keeps the product category menus (but simplifies them), allows certain products to be featured, and has a simple CTA box (something like "Login" for existing wholesale customers or "Start a Business" for new customers). The layout might be something along the lines of http://www.pinewellmarket.com/ except with a shopping cart featured at the top right. Our colors tend to be earth-toned, but the current color palate looks dated. Also see our blog.lomatrade.com page for themes and color ideas that are maybe more up-to-date. On our product pages, we want to feature the products more prominently and have simpler, cleaner Buy or Add buttons.

Other reference sites for inspiration: dravensupply.com, kettlorhome.com, http://www.pinewellmarket.com, http://morvanbulkgoods.com/ http://tenubra.com/
Updates

Project Deadline Extended
Reason: We like many of the designs that have been submitted so far, but need more time to make our final choice.

Target Market(s)

Small wholesale customers, most have a small business or home-based business. Also some retail, so an option for retail customers to click at the top to see retail pricing would be nice

Industry/Entity Type

Wholesale

Number of Pages Required

3 page

Font styles to use
Sans Serif

Requirements
Must have
• Clean, clear design that highlights products and reduces friction to customer purchase. Should include one homepage, one product page, and one shopping cart page design. Works with all browser types and be mobile-friendly.
Nice to have
• Other color schemes that would look good with our logo (maybe different from colors chosen below).
Should not have
• Splash pages with special effects, Adobe flash, elements that slow down page load times or that only work well in certain browsers.

```html
<!DOCTYPE html>
<html lang="en">
<head>
<meta charset="utf-8">
<title>Loma Trade — Wholesale African Goods</title>
<link href="https://fonts.googleapis.com/css2?family=Roboto:wght@300;400;500;700&family=Roboto+Slab:wght@300;400;700&display=swap" rel="stylesheet">
<style>
  :root{
    --red:#d9342b;
    --gold:#d4952e;
    --ink:#222;
    --muted:#555;
    --line:#dcdcdc;
    --nav-bg:#ececec;
    --white:#fff;
  }
  *{box-sizing:border-box;margin:0;padding:0}
  html,body{width:960px;height:1200px;overflow:hidden;background:var(--white)}
  body{position:relative;font-family:'Roboto',sans-serif;color:var(--ink)}
  .abs{position:absolute}

  .topbar{left:0;top:0;width:960px;height:36px;border-bottom:1px solid var(--line);font-size:12px;color:var(--muted)}
  .topbar a{position:absolute;top:11px;display:flex;align-items:center;gap:5px;color:var(--muted);text-decoration:none}
  .topbar svg{width:10px;height:10px;fill:var(--red)}
  .topbar .signup{color:var(--red)}

  .header{left:0;top:36px;width:960px;height:74px}
  .brand{left:32px;top:20px;width:70px;display:flex;align-items:center;gap:5px;font-weight:700;font-size:12px;line-height:14px;color:var(--ink);letter-spacing:.5px}
  .brand .mark{flex:none;width:10px;height:10px;border-radius:50%;background:var(--red)}
  .search{left:110px;top:21px;width:374px;height:30px;border:1px solid var(--line);font-size:11px;color:#999;padding:8px 10px;letter-spacing:.3px}
  .search svg{position:absolute;right:12px;top:9px;width:12px;height:12px}
  .contact{left:550px;top:17px;font-size:11.5px;line-height:18px;color:#333}
  .contact div{display:flex;align-items:center;gap:8px}
  .contact svg{width:12px;height:12px}
  .divider{left:758px;top:12px;width:1px;height:46px;background:var(--line)}
  .cart-icon{left:773px;top:16px;width:36px;height:36px}
  .cart-info{left:822px;top:14px;width:110px;font-size:9.5px;color:#333}
  .cart-info p{font-size:8px;color:#999;line-height:9.5px;margin-top:6px}

  .nav{left:0;top:110px;width:960px;height:39px;background:var(--nav-bg);font-size:10.5px;color:#333}
  .nav span{position:absolute;top:15px;letter-spacing:.2px}

  .hero{left:0;top:150px;width:960px;height:300px;background:linear-gradient(100deg,#7a6a55 0%,#b79b74 30%,#8a6c3e 50%,#6b5a47 75%,#b7a994 100%)}
  .hero-panel{left:6px;top:76px;width:334px;height:128px;background:rgba(203,112,56,.85)}
  .hero-title{left:32px;top:96px;color:var(--white);font-family:'Roboto Slab',serif;font-size:32px;line-height:38px}
  .hero-title .l1{font-weight:300;font-family:'Roboto',sans-serif}
  .hero-title .l2{font-weight:700}
  .btn{position:absolute;display:flex;align-items:center;justify-content:center;color:var(--white);font-size:11.5px;font-weight:500;letter-spacing:.3px}
  .btn-red{background:var(--red)}
  .btn-gold{background:var(--gold)}
  .dots{left:463px;top:280px;display:flex;gap:3px}
  .dots i{width:8px;height:8px;border-radius:50%;border:1px solid var(--red)}
  .dots i:first-child{background:var(--red)}

  .tile{position:absolute;overflow:hidden}
  .tile-title{position:absolute;font-family:'Roboto Slab',serif;font-size:30px;font-weight:400;color:#111;white-space:nowrap}
  .soaps{left:0;top:454px;width:480px;height:336px;background:linear-gradient(135deg,#6e5a44 0%,#8a7560 45%,#e9e6e2 80%,#f5f4f2 100%)}
  .oils{left:480px;top:454px;width:480px;height:336px;background:linear-gradient(160deg,#f1f0f0 0%,#d6cde0 40%,#8b4a20 70%,#6a4aa0 100%)}
  .promo{left:0;top:790px;width:480px;height:290px;text-align:center}
  .promo h2{position:absolute;left:0;width:480px;top:64px;font-family:'Roboto Slab',serif;font-weight:400;font-size:24px;color:#111}
  .promo p{position:absolute;left:0;width:480px;top:101px;font-size:11px;line-height:19px;color:#333}
  .email{left:31px;top:159px;width:331px;height:29px;border:1px solid var(--line);font-size:11px;color:#999;padding:8px 14px;text-align:left}
  .fabrics{left:480px;top:790px;width:480px;height:290px;background:linear-gradient(120deg,#e0742a 0%,#2a7a3a 25%,#c7a020 45%,#1a3c8a 65%,#d24a2a 85%,#e8b23a 100%)}
  .artwork{left:0;top:1080px;width:480px;height:120px;background:linear-gradient(90deg,#8a4a2a 0%,#d7763f 40%,#e89a6a 70%,#b25a32 100%)}
  .shea{left:480px;top:1080px;width:480px;height:120px;background:linear-gradient(110deg,#eeeeec 0%,#e6e3de 50%,#d8cbbd 100%)}
</style>
</head>
<body>

<nav class="abs topbar">
  <a style="left:32px"><svg viewBox="0 0 10 10"><circle cx="5" cy="5" r="5"/></svg>About</a>
  <a style="left:97px"><svg viewBox="0 0 10 10"><path d="M0 1h2l1 5h6l1-4H3"/><circle cx="4" cy="8.5" r="1"/><circle cx="8" cy="8.5" r="1"/></svg>Quick Order</a>
  <a style="left:187px"><span style="color:var(--red)">$</span>Retail Pricing</a>
  <a style="left:282px"><svg viewBox="0 0 10 10"><circle cx="5" cy="5" r="5"/></svg>My Account</a>
  <a style="left:373px"><svg viewBox="0 0 10 10"><rect y="1.5" width="10" height="7"/></svg>Contact us</a>
  <a style="left:804px"><svg viewBox="0 0 10 10"><path d="M1 1h8v8H1z" fill="none" stroke="#d9342b"/><path d="M3 5h4" stroke="#d9342b"/></svg>Sign in</a>
  <a class="signup" style="left:875px"><svg viewBox="0 0 10 10"><circle cx="5" cy="3" r="2.5"/><path d="M0 10c0-3 2-4.5 5-4.5S10 7 10 10z"/></svg>Sign up</a>
</nav>

<header class="abs header">
  <div class="abs brand"><span class="mark"></span><span>LOMA<br>TRADE</span></div>
  <div class="abs search">KEYWORD SEARCH OR ITEM #
    <svg viewBox="0 0 12 12"><circle cx="5" cy="5" r="4" fill="none" stroke="#999" stroke-width="1.4"/><path d="M8 8l3.5 3.5" stroke="#999" stroke-width="1.4"/></svg>
  </div>
  <div class="abs contact">
    <div><svg viewBox="0 0 12 12"><path d="M2 1l2 0 1 3-1.5 1a6 6 0 0 0 3.5 3.5L8 7l3 1v2c0 1-1 1-2 1A9 9 0 0 1 1 3c0-1 0-2 1-2z" fill="#d9342b"/></svg>TOLL FREE: (800) 555-0142</div>
    <div><svg viewBox="0 0 12 12"><circle cx="6" cy="6" r="5" fill="none" stroke="#d9342b" stroke-width="1.3"/><path d="M6 3v3.5h2.5" fill="none" stroke="#d9342b" stroke-width="1.3"/></svg>Mon-Fri: 9.00-19.00</div>
  </div>
  <div class="abs divider"></div>
  <svg class="abs cart-icon" viewBox="0 0 36 36"><path d="M1 5h6l4 18h20l4-14H9" fill="none" stroke="#d9342b" stroke-width="3"/><path d="M10 10h24l-3 11H12z" fill="#d9342b"/><circle cx="14" cy="30" r="3" fill="#d9342b"/><circle cx="29" cy="30" r="3" fill="#d9342b"/></svg>
  <div class="abs cart-info"><b>0</b> items<p>This order will provide 0 meals for children in Africa</p></div>
</header>

<div class="abs nav">
  <span style="left:32px">CLOTHING ⌄</span>
  <span style="left:128px">FABRIC ⌄</span>
  <span style="left:207px">OILS ⌄</span>
  <span style="left:274px">HEALTH&amp;BEAUTY ⌄</span>
  <span style="left:402px">SOAP ⌄</span>
  <span style="left:474px">MUSIC INSTRUMENTS ⌄</span>
  <span style="left:622px">ART ⌄</span>
  <span style="left:688px">ACCESSORIES ⌄</span>
  <span style="left:799px">NEW</span>
</div>

<section class="abs hero" role="img" aria-label="Photo of shea butter, argan nuts and oil bottle on burlap">
  <div class="abs hero-panel"></div>
  <h1 class="abs hero-title"><span class="l1">Start Your Own</span><br><span class="l2">African Business</span></h1>
  <div class="btn btn-red" style="left:32px;top:215px;width:131px;height:39px">FIND OUT MORE &nbsp;»</div>
  <div class="abs dots"><i></i><i></i><i></i></div>
</section>

<section class="tile soaps" role="img" aria-label="Photo of African black soap blocks with leaves">
  <h2 class="tile-title" style="left:32px;top:242px">AFRICAN SOAPS</h2>
  <div class="btn btn-gold" style="left:32px;top:285px;width:131px;height:39px">GO TO SOAPS</div>
</section>

<section class="tile oils" role="img" aria-label="Photo of amber essential oil bottles with lavender">
  <h2 class="tile-title" style="left:16px;top:22px">ESSENTIAL OIL</h2>
  <div class="btn btn-gold" style="left:17px;top:68px;width:131px;height:40px">GO TO OILS</div>
</section>

<section class="tile promo">
  <h2>SIGN UP FOR OUR PROMOTIONS!</h2>
  <p>Find new customers the best way with this free six-lesson e-mail course.<br>You'll get one new e-mail each day!</p>
  <div class="abs email">ENTER YOUR EMAIL</div>
  <div class="btn btn-red" style="left:362px;top:159px;width:91px;height:29px">SIGN UP</div>
</section>

<section class="tile fabrics" role="img" aria-label="Photo of colourful African wax print fabrics">
  <h2 class="tile-title" style="left:190px;top:180px">AFRICAN FABRICS</h2>
  <div class="btn btn-gold" style="left:317px;top:230px;width:131px;height:39px">GO TO OILS</div>
</section>

<section class="tile artwork" role="img" aria-label="Photo of carved African artwork and baskets">
  <h2 class="tile-title" style="left:164px;top:10px">AFRICAN ARTWORK</h2>
  <div class="btn btn-gold" style="left:318px;top:74px;width:128px;height:40px">GO TO SOAPS</div>
</section>

<section class="tile shea" role="img" aria-label="Photo of whipped shea butter with white flowers"></section>

</body>
</html>
```